Structural Engineering Business Card

Veltrow Drafts does residential house plans for clients in Central Florida. Would like simple but elegant business card that is appropriate for a house plan engineering company. Prefer black business card with black/white them but open to other shades of blue. I uploaded a sample card that I came across that looked good but please come up with your own creative designs.

Contact Information for Business Card

Name, Title, Phone, Email, Address, website

```html
<!DOCTYPE html>
<html lang="en">
<head>
<meta charset="utf-8">
<title>Veltrow Drafts – Business Card</title>
<link rel="stylesheet" href="https://fonts.googleapis.com/css2?family=Fira+Sans:wght@400;700;800&display=swap">
<style>
  :root {
    --backdrop: #8c8c90;
    --card: #22187a;
    --card-deep: #1c1468;
    --ink: #ffffff;
    --ink-soft: #d9d6f2;
    --emboss: #1a125e;
    --drawing-light: #3a31a0;
  }
  * { margin: 0; padding: 0; box-sizing: border-box; }
  html, body {
    width: 1200px; height: 781px; overflow: hidden;
    background: var(--backdrop);
    font-family: "Fira Sans", sans-serif;
  }
  .sheet {
    width: 1200px; height: 781px;
    display: flex; align-items: center; justify-content: center; gap: 60px;
  }
  .card {
    position: relative;
    width: 520px; height: 297px;
    border-radius: 22px;
    background: var(--card);
    overflow: hidden;
  }
  .card-front .contact {
    position: absolute; left: 30px; top: 28px; color: var(--ink);
  }
  .person-name {
    font-weight: 800; font-size: 22px; letter-spacing: 0.5px; line-height: 1;
  }
  .person-title { font-size: 11px; margin-top: 4px; color: var(--ink-soft); }
  .brand-name {
    font-weight: 800; font-size: 16px; margin-top: 20px; text-transform: uppercase;
    letter-spacing: 0.3px;
  }
  .address { font-size: 12.5px; line-height: 1.35; margin-top: 8px; }
  .details { list-style: none; margin-top: 12px; font-size: 12.5px; line-height: 1.45; }
  .details li { display: flex; align-items: center; gap: 7px; }
  .details svg { width: 11px; height: 11px; flex: none; }
  .house-drawing {
    position: absolute; left: 270px; top: 84px; width: 226px; height: 190px;
    border-radius: 4px;
    background: linear-gradient(135deg, var(--card) 0%, var(--drawing-light) 55%, var(--card) 100%);
  }
  .card-back { display: flex; align-items: center; justify-content: center; background: var(--card-deep); }
  .back-brand {
    font-weight: 800; font-size: 50px; text-transform: uppercase;
    color: var(--emboss); letter-spacing: 1px;
  }
</style>
</head>
<body>
<main class="sheet">
  <section class="card card-front">
    <div class="contact">
      <div class="person-name">MARCUS ELLERY</div>
      <div class="person-title">Manager</div>
      <div class="brand-name">Veltrow Drafts</div>
      <div class="address">1450 Orchard Lane Ste 2<br>Lake Vista, FL 32801</div>
      <ul class="details">
        <li><svg viewBox="0 0 12 12" fill="none" stroke="#fff" stroke-width="1.2"><rect x="3" y="1" width="6" height="10" rx="1"/><line x1="5" y1="9" x2="7" y2="9"/></svg>407-555-0182</li>
        <li><svg viewBox="0 0 12 12" fill="none" stroke="#fff" stroke-width="1.2"><path d="M2 1.5 L4 1.5 L5 4 L3.8 5 Q5 7.5 7 8.2 L8 7 L10.5 8 L10.5 10 Q6 11 3 7.5 Q1 4.5 2 1.5Z"/></svg>407-555-0147</li>
        <li><svg viewBox="0 0 12 12" fill="none" stroke="#fff" stroke-width="1.2"><rect x="1" y="2.5" width="10" height="7"/><path d="M1 2.5 L6 6.5 L11 2.5"/></svg>info@veltrowdrafts.com</li>
        <li><svg viewBox="0 0 12 12" fill="none" stroke="#fff" stroke-width="1.1"><circle cx="6" cy="6" r="5"/><ellipse cx="6" cy="6" rx="2.2" ry="5"/><line x1="1" y1="6" x2="11" y2="6"/></svg>veltrowdrafts.com</li>
      </ul>
    </div>
    <div class="house-drawing" role="img" aria-label="Fine white line architectural elevation drawing of a house with pitched roof and dimension lines"></div>
  </section>
  <section class="card card-back">
    <div class="back-brand">Veltrow Drafts</div>
  </section>
</main>
</body>
</html>
```